Quindral Professional Services Website

Small website for company presence and information. Company is an IT/Telecom services company. We provide presales and installation services. Included are various company logos including color levels. Site doesn't have to use these exact colors in the logos, but should be complimentary if using different colors. It should have a professional business appearance.
Updates

My apologies for not being more responsive on the designs that have been submitted. I will be narrowing down the submissions and providing additional feedback next week. Thank you for your patience.

Project Deadline Extended
Reason: Sorry again for delays on picking designs. Work has me very busy and I've just not had the time to devote to this project. I am extending the design deadline for a few more days to give me time to make my final decisions. Thank you all for your patience. Stay tuned....

Target Market(s)

Telecom sales companies that sell Brintel telecom products.

Industry/Entity Type

Professional Service

Coding

Coded - Design and coding required

Number of Pages Required

5+ page

Font styles to use
Sans Serif

Colors
3276b5
0355a3
85abd2
85cae6
33a6d7
0692cd
ffffff

Requirements
Must have
• Professional design reflective of IT/Telecom business. A good reference website would be: http://www.quollanetworks.example/. Looking for something similar in function and presence.
Nice to have
• Rolling photos highlighting our services. Traditional navigation across the top of all pages.
Should not have
• No motion video, flashy presentation or overly confused interface.

```html
<!DOCTYPE html>
<html lang="en">
<head>
<meta charset="utf-8">
<title>Quindral Professional Services</title>
<link rel="stylesheet" href="https://fonts.googleapis.com/css2?family=Open+Sans:ital,wght@0,400;0,600;0,700;1,400;1,700&display=swap">
<style>
:root{
  --blue:#1f72b6;
  --blue-dark:#0355a3;
  --blue-mid:#3276b5;
  --blue-light:#85abd2;
  --sky:#0692cd;
  --ink:#3c4650;
  --text:#6b737a;
  --muted:#9aa0a6;
  --page:#f2f2f2;
  --band:#e8e8e8;
  --card:#ffffff;
  --btn-grey:#d4d4d4;
  --red:#e04848;
  --white:#ffffff;
}
*{box-sizing:border-box;margin:0;padding:0}
html,body{width:715px;height:1200px;overflow:hidden}
body{position:relative;background:var(--page);font-family:"Open Sans",Arial,sans-serif;color:var(--text);font-size:7px;line-height:1.5}
a{text-decoration:none}
.abs{position:absolute}

/* header */
.site-header{left:0;top:0;width:715px;height:38px;background:#eeeeee;border-bottom:1px solid #e0e0e0}
.brand{left:78px;top:8px;display:flex;align-items:center;gap:5px}
.brand-square{width:20px;height:20px;background:var(--blue)}
.brand-name{font-weight:700;font-size:15px;line-height:1;color:var(--blue-dark);letter-spacing:1px}
.brand-sub{font-size:5px;font-weight:600;letter-spacing:1.2px;color:var(--sky);line-height:1.3}
.main-nav{right:78px;top:11px;display:flex;align-items:center;gap:6px}
.main-nav a{font-size:6px;font-weight:600;color:var(--ink);padding:4px 10px;border-radius:2px}
.main-nav a.is-home{background:#b9b9b9;color:var(--white)}
.main-nav a.is-active{background:var(--blue);color:var(--white);padding:4px 14px}
.search-icon{width:8px;height:8px}

/* hero */
.hero{left:0;top:38px;width:715px;height:238px;background:radial-gradient(ellipse at 70% 40%,#3a4654 0%,#1c232c 55%,#0d1117 100%)}
.hero-caption{left:73px;top:51px;width:372px;height:115px;background:rgba(31,114,182,.82);padding:6px 6px}
.hero-caption h1{font-size:13px;font-style:italic;font-weight:700;color:var(--white);line-height:1.3;margin-bottom:5px}
.hero-caption p{font-size:7.3px;color:#e9f1f8;line-height:1.68}
.hero-dots{left:339px;top:222px;display:flex;gap:3px}
.hero-dots span{width:7px;height:7px;background:var(--sky)}
.hero-dots span:first-child{background:var(--white)}

/* services */
.services-bar{left:78px;top:301px;width:557px;height:46px;background:#e6e6e6;padding:9px 13px}
.services-bar h2{font-size:14px;font-weight:400;color:#5e666d;line-height:1.2}
.services-bar p{font-size:5.8px;color:var(--muted)}
.btn{display:inline-block;text-align:center;font-weight:600;color:var(--white);border-radius:2px}
.btn-primary{background:var(--blue);box-shadow:0 2px 0 #15598f}
.view-more{right:17px;top:11px;width:95px;height:25px;line-height:25px;font-size:9px}
.service-card{top:372px;width:129px;height:150px;background:#f6f6f6;text-align:center;padding-top:20px}
.service-card.is-featured{background:var(--card);box-shadow:0 1px 3px rgba(0,0,0,.08)}
.service-card svg{width:40px;height:30px}
.service-card h3{font-size:7.4px;font-weight:700;color:#5e666d;margin:8px 0 8px}
.service-card p{font-size:5.8px;color:var(--muted);padding:0 10px;line-height:1.7}
.read-more{position:absolute;left:17px;bottom:-2px;width:95px;height:25px;line-height:25px;font-size:6.4px;font-weight:400;background:var(--btn-grey);box-shadow:0 2px 0 #bdbdbd}
.is-featured .read-more{background:var(--blue);box-shadow:0 2px 0 #15598f}

/* why us */
.why-band{left:0;top:557px;width:715px;height:191px;background:var(--band)}
.why-title{left:0;top:571px;width:715px;text-align:center;font-size:19px;font-weight:600;color:var(--blue-mid)}
.why-text{left:80px;top:602px;width:558px;text-align:center;font-size:6.4px;color:var(--muted);line-height:1.65}
.team-photo{left:250px;top:652px;width:194px;height:172px;border-radius:40% 40% 8px 8px / 30% 30% 8px 8px;background:linear-gradient(180deg,rgba(60,64,72,0) 0%,#3a3e46 22%,#2c3038 70%,rgba(150,150,150,.35) 100%)}

/* columns */
.col-title{font-size:7.4px;font-weight:700;color:#5e666d}
.choose{left:78px;top:849px;width:120px}
.choose ul{list-style:none;margin-top:13px}
.choose li{font-size:5.9px;color:var(--text);margin-bottom:4.3px;display:flex;align-items:center;gap:4px}
.choose li::before{content:"";width:0;height:0;border-left:4px solid var(--sky);border-top:2.5px solid transparent;border-bottom:2.5px solid transparent}
.intro{left:231px;top:846px;width:250px}
.intro p{font-size:6.2px;color:var(--text);line-height:1.72}
.intro a{color:var(--red);text-decoration:underline}
.start-today{left:318px;top:915px;width:78px;height:25px;line-height:25px;font-size:8.5px}
.testimonial{left:505px;top:849px;width:130px}
.quote{margin-top:10px;background:var(--white);padding:6px 9px;font-size:5.8px;font-style:italic;color:var(--muted);line-height:1.75}
.quote-author{font-size:7px;color:var(--ink);margin:4px 0 0 30px}

/* clients */
.clients-title{left:78px;top:971px}
.clients-rule{left:160px;top:977px;width:420px;height:1px;background:#dedede}
.arrow-btn{top:968px;width:19px;height:19px;border-radius:2px}
.arrow-btn svg{width:19px;height:19px}
.arrow-prev{left:587px;background:#8f9a9a}
.arrow-next{left:616px;background:var(--red)}
.client-row{left:78px;top:1006px;display:flex;gap:14px}
.client{width:81px;height:43px;background:var(--white);display:flex;align-items:center;justify-content:center;gap:4px;font-size:10px;font-weight:600;color:#6b6b6b;white-space:nowrap}
.client i{width:8px;height:8px;background:#8a8a8a;display:block}

/* footer */
.site-footer{left:0;top:1073px;width:715px;height:127px;background:var(--blue);color:#e6eff8}
.footer-brand{left:80px;top:17px;display:flex;align-items:center;gap:5px}
.footer-brand .brand-square{background:var(--white)}
.footer-brand .brand-name{color:var(--white)}
.footer-brand .brand-sub{color:#d7e6f3}
.footer-about{left:80px;top:52px;width:180px;font-size:5.9px;line-height:1.85}
.contact-line{left:80px;display:flex;align-items:baseline;gap:7px;font-size:5.9px}
.contact-line b{font-size:9.5px;font-style:italic;font-weight:600;color:var(--white)}
.footer-col{top:23px}
.footer-col h4{font-size:8.8px;font-weight:600;color:#b7d0e6;margin-bottom:7px}
.footer-col ul{list-style:none}
.footer-col li{font-size:5.9px;margin-bottom:3.4px;padding-left:8px;position:relative}
.footer-col li::before{content:"›";position:absolute;left:0;top:-1px}
.social li{padding-left:13px;margin-bottom:6px}
.social li::before{content:"";width:7px;height:7px;background:var(--white);top:1px}
.copyright{left:460px;top:100px;font-size:5.4px;line-height:1.9}
</style>
</head>
<body>

<header class="site-header abs">
  <div class="brand abs">
    <span class="brand-square"></span>
    <div><div class="brand-name">QUINDRAL</div><div class="brand-sub">PROFESSIONAL SERVICES</div></div>
  </div>
  <nav class="main-nav abs">
    <a href="#" class="is-home">HOME</a>
    <a href="#">ABOUT</a>
    <a href="#">SERVICES</a>
    <a href="#" class="is-active">PORTFOLIO</a>
    <a href="#">CONTACTS</a>
    <svg class="search-icon" viewBox="0 0 10 10"><circle cx="4" cy="4" r="3" fill="none" stroke="#3c4650" stroke-width="1.4"/><line x1="6.2" y1="6.2" x2="9.2" y2="9.2" stroke="#3c4650" stroke-width="1.6"/></svg>
  </nav>
</header>

<section class="hero abs" role="img" aria-label="Dark world map with glowing network connection lines">
  <div class="hero-caption abs">
    <h1>Lorem ipsum dolor sit amet, consectetuer adipiscing</h1>
    <p>Lorem ipsum dolor sit amet, consectetuer adipiscing elit, sed diam nonummy nibh euismod tincidunt ut laoreet dolore magna aliquam erat volutpat. Ut wisi enim ad minim veniam, quis nostrud exerci tation ullamcorper suscipit lobortis nisl ut aliquip ex ea commodo consequat. Duis autem vel eum iriure dolor in hendrerit in vulputate velit esse molestie consequat, vel illum dolore eu feugiat nulla facilisis at vero eros et accumsan et iusto odio dignissim qui blandit praesent luptatum zzril delenit augue duis dolore te feugait nulla facilisi.</p>
  </div>
  <div class="hero-dots abs"><span></span><span></span><span></span><span></span></div>
</section>

<section class="services-bar abs">
  <h2>Some of our top services</h2>
  <p>Ut eleifend libero sed neque rhoncus consequat. Maecenas tincidunt, augue et rutrum condimentum, libero lectus mattis orci, ut commodo.</p>
  <a href="#" class="btn btn-primary view-more abs">VIEW MORE</a>
</section>

<article class="service-card is-featured abs" style="left:78px">
  <svg viewBox="0 0 40 30"><g fill="#5e666d"><rect x="10" y="1" width="20" height="5"/><rect x="7" y="8" width="26" height="5"/><rect x="7" y="15" width="26" height="5"/><rect x="10" y="22" width="20" height="5"/><rect x="2" y="28" width="36" height="1.5"/></g><g fill="#fff"><rect x="12" y="3" width="10" height="1"/><rect x="9" y="10" width="14" height="1"/><rect x="9" y="17" width="14" height="1"/><rect x="12" y="24" width="10" height="1"/></g></svg>
  <h3>Data Center Solutions</h3>
  <p>Quisque id tellus quis risus vehicula vehicula ut turpis. In eros nulla, placerat vitae at, vehicula ut nunc.</p>
  <a href="#" class="btn read-more">read more</a>
</article>
<article class="service-card abs" style="left:221px">
  <svg viewBox="0 0 40 30"><rect x="9" y="2" width="22" height="15" fill="none" stroke="#b5b5b5" stroke-width="1.5"/><line x1="20" y1="17" x2="20" y2="25" stroke="#b5b5b5" stroke-width="1.5"/><line x1="5" y1="25" x2="35" y2="25" stroke="#b5b5b5" stroke-width="1.5"/><rect x="17" y="23" width="6" height="4" fill="#b5b5b5"/></svg>
  <h3>Unified Workspace</h3>
  <p>Ut eleifend libero sed neque rhoncus consequat. Maecenas tincidunt, augue et rutrum condimentum, libero lectus mattis orci, ut commodo.</p>
  <a href="#" class="btn read-more">read more</a>
</article>
<article class="service-card abs" style="left:364px">
  <svg viewBox="0 0 40 30"><path d="M10 20a6 6 0 0 1 1-12 8 8 0 0 1 15-2 7 7 0 0 1 5 14z" fill="#b5b5b5"/><line x1="20" y1="20" x2="20" y2="26" stroke="#b5b5b5" stroke-width="1.5"/><circle cx="20" cy="27" r="2" fill="#b5b5b5"/><line x1="12" y1="27" x2="28" y2="27" stroke="#b5b5b5" stroke-width="1"/></svg>
  <h3>Cloud Services</h3>
  <p>Vivamus eget ante bibendum arcu vehicula ultricies. Integer venenatis mattis nisl, vitae pulvinar dui tempor non.</p>
  <a href="#" class="btn read-more">read more</a>
</article>
<article class="service-card abs" style="left:506px">
  <svg viewBox="0 0 40 30"><path d="M20 1l11 4v9c0 8-5 12-11 15C14 26 9 22 9 14V5z" fill="#b5b5b5"/><path d="M15 15l4 4 7-8" fill="none" stroke="#fff" stroke-width="2.4"/></svg>
  <h3>Security &amp; Risk Management</h3>
  <p>Astehicula ultricies. Integer venenatis mattis nisl, vitae pulvinar dui tempor non.</p>
  <a href="#" class="btn read-more">read more</a>
</article>

<div class="why-band abs"></div>
<h2 class="why-title abs">Why Us?</h2>
<p class="why-text abs">Lorem ipsum dolor sit amet, consectetuer adipiscing elit, sed diam nonummy nibh euismod tincidunt ut laoreet dolore magna aliquam erat volutpat. Ut wisi enim ad minim veniam, quis nostrud exerci tation ullamcorper suscipit lobortis nisl ut aliquip ex ea commodo consequat. Duis autem vel eum iriure dolor in hendrerit in vulputate velit esse molestie consequat, vel illum dolore eu feugiat nulla facilisis at vero eros et accumsan et iusto odio dignissim qui blandit praesent luptatum zzril delenit augue duis dolore te feugait nulla facilisi.</p>
<div class="team-photo abs" role="img" aria-label="Group of business professionals standing together in suits"></div>

<section class="choose abs">
  <h3 class="col-title">Why Choose Us ?</h3>
  <ul>
    <li>Quisque at massa ipsum</li>
    <li>Maecenas a lorem augue, egestas</li>
    <li>Cras vitae felis at lacus eleifend</li>
    <li>Etiam auctor diam pellentesque</li>
    <li>Nulla ac massa at dolor</li>
    <li>Condimentum eleifend vitae vitae</li>
  </ul>
</section>
<section class="intro abs">
  <p>Curabitur quis nisl in leo euismod venenatis eu in diam. Etiam auctor diam pellentesque lectus <a href="#">vehicula mattis</a>. Nulla ac massa at dolor condiLorem ipsum dolor sit amet, consectetuer adipiscing elit, sed diam nonummy nibh euismod tincidunt ut laoreet dolore magna aliquam erat volutpat. Ut wisi enim ad minim veniam, quis nostrud exerci tation ullamcorper suscipit lomentum eleifend vitae vitae urna.</p>
</section>
<a href="#" class="btn btn-primary start-today abs">START TODAY</a>
<section class="testimonial abs">
  <h3 class="col-title">What Client's Say ?</h3>
  <blockquote class="quote">Curabitur quis nisl in leo euismod venenatis eu in diam. Etiam auctor diam pellentesque lectus vehicula mattis. Nulla ac massa at dolor condimentum</blockquote>
  <p class="quote-author">Jhon Doe</p>
</section>

<h3 class="col-title clients-title abs">Our Happy Clients</h3>
<div class="clients-rule abs"></div>
<a href="#" class="arrow-btn arrow-prev abs"><svg viewBox="0 0 19 19"><path d="M11 6l-3.5 3.5L11 13" fill="none" stroke="#fff" stroke-width="2"/></svg></a>
<a href="#" class="arrow-btn arrow-next abs"><svg viewBox="0 0 19 19"><path d="M8 6l3.5 3.5L8 13" fill="none" stroke="#fff" stroke-width="2"/></svg></a>
<div class="client-row abs">
  <div class="client"><i></i>Northwind</div>
  <div class="client">Ketrel</div>
  <div class="client">Brakston</div>
  <div class="client">Auslane</div>
  <div class="client">Indora</div>
  <div class="client">Apsen</div>
</div>

<footer class="site-footer abs">
  <div class="footer-brand abs">
    <span class="brand-square"></span>
    <div><div class="brand-name">QUINDRAL</div><div class="brand-sub">PROFESSIONAL SERVICES</div></div>
  </div>
  <p class="footer-about abs">Lorem ipsum dolor sit amet, consectetur adipiscing elit. Nam viverra euismod odio, gravida pellentesque urna varius vitae. Sed dui lorem, adipiscing in adipiscing et, interdum nec.</p>
  <p class="contact-line abs" style="top:96px">Phone: <b>555 012 3456</b></p>
  <p class="contact-line abs" style="top:110px">e-mail: <b>abc@quindralmail.example</b></p>
  <nav class="footer-col abs" style="left:269px">
    <h4>Company</h4>
    <ul><li>About</li><li>FAQ</li><li>Contact</li><li>Terms</li><li>Privacy</li><li>Testimonials</li></ul>
  </nav>
  <nav class="footer-col abs" style="left:364px">
    <h4>Community</h4>
    <ul><li>Blog</li><li>Forum</li><li>Support</li><li>Newsletter</li></ul>
  </nav>
  <nav class="footer-col social abs" style="left:460px">
    <h4>Connect with Us</h4>
    <ul><li>Friendnet</li><li>Circlecast</li><li>Chirpline</li></ul>
  </nav>
  <p class="copyright abs">© 2017 Quindral Professional Services<br>All Rights Reserved</p>
</footer>

</body>
</html>
```